217 Marlow Lane Residences

designing a sign for apartment complex;
prefer colors gray white and yellow

Target Market(s)

residents coming home to their apartment

Font styles to use
Serif
Sans Serif

Colors
FFF300
FFF600
FEFA6F
FFFEC7
FFFEE8

Requirements
Must have
• black or gray, white and some yellow; easy to read and see

```html
<!DOCTYPE html>
<html lang="en">
<head>
<meta charset="utf-8">
<title>217 Marlow Lane Residences — Sign</title>
<link href="https://fonts.googleapis.com/css2?family=Tinos:wght@700&display=swap" rel="stylesheet">
<style>
  :root {
    --page-bg: #ffffff;
    --frame-gray: #b3b4b3;
    --trim-white: #ffffff;
    --sign-yellow: #fff300;
    --ink: #262626;
    --shadow: rgba(0, 0, 0, 0.35);
  }
  html, body {
    margin: 0;
    padding: 0;
    width: 1200px;
    height: 1200px;
    overflow: hidden;
    background: var(--page-bg);
  }
  .sign {
    display: block;
    width: 1200px;
    height: 1200px;
  }
  .sign__frame {
    fill: var(--frame-gray);
    filter: drop-shadow(0 22px 16px var(--shadow));
  }
  .sign__face {
    fill: var(--sign-yellow);
    stroke: var(--trim-white);
    stroke-width: 8;
  }
  .sign__rule {
    fill: none;
    stroke: var(--ink);
    stroke-width: 2.5;
  }
  .sign__ornament {
    fill: var(--ink);
    opacity: 0.16;
  }
  .sign__title {
    font-family: "Tinos", "Times New Roman", serif;
    font-weight: 700;
    font-size: 108px;
    fill: var(--ink);
    text-anchor: middle;
  }
</style>
</head>
<body>
<svg class="sign" viewBox="0 0 1200 1200" xmlns="http://www.w3.org/2000/svg">
  <path class="sign__frame"
        d="M174,346 H308 Q600,214 892,346 H1026 V420 Q1138,600 1026,780 V852 H892 Q600,988 308,852 H174 V780 Q62,600 174,420 Z"/>
  <path class="sign__face"
        d="M210,382 H310 Q600,255 890,382 H990 V460 Q1106,600 990,740 V816 H890 Q600,944 310,816 H210 V740 Q94,600 210,460 Z"/>
  <path class="sign__rule"
        d="M222,392 H312 Q600,256 888,392 H978 V466 Q1102,600 978,734 V804 H888 Q600,940 312,804 H222 V734 Q98,600 222,466 Z"/>

  <rect class="sign__ornament" role="img" aria-label="Decorative scrollwork flourish with fleur-de-lis"
        x="392" y="352" width="412" height="128" rx="40"/>
  <rect class="sign__ornament" role="img" aria-label="Decorative calligraphic flourish"
        x="422" y="732" width="354" height="120" rx="40"/>

  <text class="sign__title" x="600" y="594">217 Marlow</text>
  <text class="sign__title" x="600" y="690">Lane Residences</text>
</svg>
</body>
</html>
```